Holistic massage therapist

I need a business card for a business made by me, I m an holistic massage therapist, I 'm qualified in reflexology , indian head massage and sweedish body massage, I m working from home or mobile as well, i use massage as a therapy not as a beauty treatment, i m base in London.
I also offer skincare product such as creams or oils and blending with essential oil that I make my self they are completely natural and 100% use of organic product, all the product they are homemade by me.

Industry/Entity Type

Massage

Requirements
Must have
• image that express peace and quite as the massage is an anti stresful remedies for the everyday life

```html
<!DOCTYPE html>
<html lang="en">
<head>
<meta charset="utf-8">
<title>Jane Doe — Holistic Massage Therapist</title>
<link rel="stylesheet" href="https://fonts.googleapis.com/css2?family=Comfortaa:wght@300;400&display=swap">
<style>
  :root {
    --sky: #cdeaf6;
    --mist: #dcefef;
    --mint: #e6f3e6;
    --leaf: #c2dfae;
    --leaf-deep: #b5d89e;
    --ink: #3b3b3d;
  }
  html, body {
    margin: 0;
    padding: 0;
    width: 1200px;
    height: 791px;
    overflow: hidden;
  }
  .card {
    position: relative;
    width: 1200px;
    height: 791px;
    overflow: hidden;
    background: linear-gradient(115deg, var(--sky) 0%, var(--mist) 55%, var(--mint) 100%);
    font-family: "Comfortaa", "Quicksand", sans-serif;
    font-weight: 300;
    color: var(--ink);
  }
  .calm-art {
    position: absolute;
    inset: 0;
    width: 1200px;
    height: 791px;
  }
  .identity {
    position: absolute;
    left: 0;
    right: 0;
    top: 208px;
    text-align: center;
  }
  .identity__name {
    margin: 0;
    font-size: 86px;
    font-weight: 300;
    line-height: 1;
    letter-spacing: 1px;
    padding-left: 4px;
  }
  .identity__role {
    margin: 30px 0 0;
    font-size: 52px;
    font-weight: 300;
    line-height: 1;
    letter-spacing: 0.5px;
    padding-left: 16px;
  }
  .products {
    position: absolute;
    left: 44px;
    top: 508px;
    margin: 0;
    padding: 0;
    list-style: none;
  }
  .products__intro {
    font-size: 38px;
    line-height: 1;
    margin-bottom: 14px;
  }
  .products__item {
    font-size: 47px;
    line-height: 64px;
  }
  .contact {
    position: absolute;
    right: 69px;
    top: 574px;
    margin: 0;
    text-align: right;
    font-style: normal;
    font-size: 44px;
    line-height: 58px;
  }
  .contact span { display: block; }
</style>
</head>
<body>
  <main class="card">
    <svg class="calm-art" viewBox="0 0 1200 791" role="img" aria-label="Peaceful soft green swirling floral flourishes sweeping across the top right and rising from the bottom left corner">
      <defs>
        <radialGradient id="glow-top" cx="0.5" cy="0.5" r="0.5">
          <stop offset="0" stop-color="#c2dfae" stop-opacity="0.7"/>
          <stop offset="1" stop-color="#c2dfae" stop-opacity="0"/>
        </radialGradient>
        <radialGradient id="glow-bottom" cx="0.5" cy="0.5" r="0.5">
          <stop offset="0" stop-color="#c2dfae" stop-opacity="0.75"/>
          <stop offset="1" stop-color="#c2dfae" stop-opacity="0"/>
        </radialGradient>
        <linearGradient id="sweep" x1="0" y1="0" x2="1" y2="0">
          <stop offset="0" stop-color="#c2dfae" stop-opacity="0"/>
          <stop offset="0.35" stop-color="#c2dfae" stop-opacity="0.55"/>
          <stop offset="1" stop-color="#b5d89e" stop-opacity="0.8"/>
        </linearGradient>
      </defs>
      <ellipse cx="880" cy="170" rx="430" ry="230" fill="url(#glow-top)"/>
      <path d="M350 230 C 520 330, 760 250, 940 170 C 1050 125, 1140 140, 1200 150 L 1200 185 C 1130 170, 1050 165, 950 205 C 770 285, 530 350, 350 230 Z" fill="url(#sweep)"/>
      <ellipse cx="150" cy="690" rx="300" ry="230" fill="url(#glow-bottom)"/>
    </svg>

    <header class="identity">
      <h1 class="identity__name">Jane Doe</h1>
      <p class="identity__role">Holistic Massage Therapist</p>
    </header>

    <ul class="products">
      <li class="products__intro">Homemade</li>
      <li class="products__item">Creams,</li>
      <li class="products__item">Oils,</li>
      <li class="products__item">Blendings</li>
    </ul>

    <address class="contact">
      <span class="contact__phone">07700 900418</span>
      <span class="contact__street">41 Willow Lane, Gravesend,</span>
      <span class="contact__town">Kent DA12, UK</span>
    </address>
  </main>
</body>
</html>
```